Environmental Consultancey needs Web Design

A consultancey firm based in Papua New Guinea specialising servicing a client market primarily in Melanesia, the wider Pacific Region and South East Asia. The firm provides services to community development and resource extraction activites that incorporate sustainable livelihoods for local customary land owners with environmentally responsibile practices and a focus on maintaining biodiversity and ecosystem services. We aim to encompass Culture, Custom and Science in our approach. Our website preferentially will convey a relaxed Pacific Island feel in its colours and design rather than a sterile corporate feel. See attached logo that will need to be visible on page or which may provide basis for ideas for the page.

Target Market(s)

Our target market is primarily the oil, gas and mining industry, secondarily international donor and aid programs followed by government projects and not for profit programs. Services include:
1. Biodiversity and Conservation - Fauna and Flora survey, assessment, management, monitoring & research, protected areas & endangered & threatend species.
2. Social & Community - impact, stakeholder engagement, census and survey, land and community affairs, capacity building empowerment.
3. Environmental Management - sustainable use, enterprise development & management, biodiversity offsets.

Industry/Entity Type

Community

Requirements
Must have
• Multiple pages, Logo somewhere on home page. Space for a couple of photos that as yet ive not decieded upon.
Nice to have
• Perhaps incorporate shapes, texture and colours that convey a feel of the attached photo of a blue bird of paradise. The blue fine overlapping and interlocking feather patterns are appealing perhaps as a background and the other colours used in boarders ? Abstract is fine as would be symbolic images or tribal ambience. The company is all about blending humanity in all its forms with the environment.

```html
<!DOCTYPE html>
<html lang="en">
<head>
<meta charset="utf-8">
<title>Kunai Environment – Culture Custom Science</title>
<link href="https://fonts.googleapis.com/css2?family=Open+Sans:wght@400;600;700&family=Arimo:wght@400;700&display=swap" rel="stylesheet">
<style>
:root{
  --green:#3f9410;
  --green-light:#6cc024;
  --teal:#0f9a8c;
  --blue:#0b78c0;
  --ink:#111;
  --muted:#777;
  --rule:#d4d4d4;
  --page:#fff;
  --sky:#5a8fc4;
  --land:#5b7a3e;
}
*{margin:0;padding:0;box-sizing:border-box}
html,body{width:1200px;height:934px;overflow:hidden}
body{position:relative;font-family:"Arimo",Arial,sans-serif;color:var(--ink)}
.scenery{position:absolute;inset:0;background:linear-gradient(180deg,var(--sky) 0%,var(--land) 100%)}
.page{position:absolute;left:255px;top:0;width:715px;height:845px;background:var(--page);box-shadow:0 0 12px rgba(0,0,0,.45)}
.abs{position:absolute}
/* header */
.brand-dot{left:24px;top:14px;width:58px;height:58px;border-radius:50%;background:var(--green)}
.brand-rule{left:132px;top:14px;width:1px;height:46px;background:var(--rule)}
.brand-name{left:144px;top:13px;font-family:"Open Sans",sans-serif;font-size:24px;font-weight:600;color:var(--ink);line-height:1.1;white-space:nowrap}
.brand-tag{left:146px;top:43px;font-family:"Open Sans",sans-serif;font-size:12px;color:var(--green);white-space:nowrap}
.util{right:14px;top:7px;font-size:9px;color:var(--muted);white-space:nowrap}
.util span{margin:0 5px}
.search{right:12px;top:37px;display:flex;align-items:center;gap:4px;font-size:10.5px;color:var(--ink)}
.search-field{width:116px;height:17px;border:1px solid #ccc;background:linear-gradient(#eee,#fff);margin-left:6px}
.search-go{height:17px;padding:0 5px;background:var(--green-light);color:#fff;font-size:10px;line-height:17px;font-weight:700}
/* nav */
.nav{left:0;top:82px;width:715px;height:38px;background:linear-gradient(#5aa81c,#2f7e0a)}
.nav ul{list-style:none;display:flex;gap:3px;padding:14px 0 0 13px}
.nav li{width:69px;height:22px;border-radius:4px 4px 0 0;background:linear-gradient(#7ed23a,#3a910e);color:#fff;font-size:10.5px;text-align:center;line-height:21px;border:1px solid #9be25c;white-space:nowrap}
/* banner */
.banner{left:11px;top:125px;width:694px;height:187px;background:#5f6a4a;box-shadow:0 0 4px rgba(0,0,0,.4)}
.banner-caption{left:379px;top:105px;width:311px;height:65px;background:var(--blue);color:#fff;font-family:"Open Sans",sans-serif;font-size:11.8px;line-height:1.15;padding:8px 9px}
.banner-timer{left:610px;top:44px;color:#9cc6ea;font-size:8px;word-spacing:38px}
/* intro */
.welcome{left:16px;top:322px;font-family:"Open Sans",sans-serif;font-size:25px;font-weight:600;color:var(--ink);white-space:nowrap}
.lead{left:18px;top:364px;width:490px;font-family:"Open Sans",sans-serif;font-size:11.6px;color:var(--green);line-height:1.22}
.intro{left:18px;top:403px;width:480px;font-size:8.2px;line-height:1.3;color:var(--ink)}
.btn{position:absolute;display:block;width:74px;height:20px;border-radius:3px;background:linear-gradient(#54a81c,#2d7a0a);color:#fff;font-size:9px;text-align:center;line-height:20px;box-shadow:0 1px 2px rgba(0,0,0,.3);white-space:nowrap}
.vrule{width:1px;background:var(--rule)}
.action{left:547px;display:flex;align-items:center;gap:6px;font-family:"Open Sans",sans-serif}
.action-icon{width:38px;height:38px;border-radius:50%}
.action-title{font-size:11px;font-weight:700;color:var(--teal);line-height:1.2}
.action-sub{font-size:11px;color:#999;line-height:1.2}
/* services */
.svc{top:514px;width:166px;height:210px}
.svc h2{font-family:"Open Sans",sans-serif;font-size:11.4px;font-weight:600;color:var(--ink);margin-bottom:9px;white-space:nowrap;letter-spacing:-.1px}
.svc-photo{width:152px;height:66px;border:3px solid #fff;box-shadow:0 0 4px rgba(0,0,0,.45)}
.svc p{font-size:9.4px;line-height:1.45;color:var(--ink);margin-top:12px;width:150px}
.svc .btn{left:0;top:182px}
/* footer */
.footer-band{left:7px;top:758px;width:701px;height:16px;background:#ebebeb}
.footer{left:0;top:774px;width:715px;height:71px;background:linear-gradient(#fff,#d6d6d6);text-align:center;font-size:9.5px;color:#555;padding-top:20px;line-height:1.7}
</style>
</head>
<body>
<div class="scenery" role="img" aria-label="Background photo of a mountain landscape with lakes"></div>
<main class="page">
  <header>
    <div class="abs brand-dot"></div>
    <div class="abs brand-rule"></div>
    <div class="abs brand-name">Kunai Environment</div>
    <div class="abs brand-tag">Culture Custom Science</div>
    <div class="abs util"><span>Home</span>|<span>SiteMap</span>|<span>Contact Us</span></div>
    <div class="abs search">Search:<div class="search-field"></div><div class="search-go">GO!</div></div>
  </header>
  <nav class="abs nav"><ul>
    <li>Home</li><li>History</li><li>About Us</li><li>What We Do</li><li>Partners</li><li>Resource</li><li>Gallery</li><li>FAQ</li><li>Contact us</li>
  </ul></nav>
  <section class="abs banner" role="img" aria-label="Photo of consultants with local people during a field visit">
    <div class="abs banner-timer">MIN SEC</div>
    <div class="abs banner-caption">Provides services to community development and resource extraction activities that incorporate sustainable livelihoods for local customary land</div>
  </section>
  <h1 class="abs welcome">Welcome to Kunai Environments</h1>
  <p class="abs lead">A consultancy firm based in Papua New Guinea specializing servicing a client market primarily in Melanesia, the wider Pacific Region and South East Asia.</p>
  <p class="abs intro">The firm provides services to community development and resource extraction activities that incorporate sustainable livelihoods for local customary land owners with environmentally responsible practices and a focus on maintaining biodiversity and ecosystem services. We aim to encompass Culture, Custom and Science in our approach. Our website preferentially will convey a relaxed Pacific Island feel in its colors and design rather than a sterile corporate feel. See attached logo that will need to be visible on page or which may provide basis for ideas for the page.</p>
  <a class="btn" style="left:16px;top:466px">READ MORE</a>
  <div class="abs vrule" style="left:532px;top:348px;height:106px"></div>
  <div class="abs action" style="top:359px">
    <div class="action-icon" style="background:#e3a520"></div>
    <div><div class="action-title">DONATE</div><div class="action-sub">Donate now and<br>support us.</div></div>
  </div>
  <div class="abs action" style="top:412px">
    <div class="action-icon" style="background:#a994e4"></div>
    <div class="action-title">SUBSCRIBE TO<br>OUR NEWSLETTER</div>
  </div>
  <div class="abs vrule" style="left:184px;top:516px;height:204px"></div>
  <div class="abs vrule" style="left:358px;top:516px;height:204px"></div>
  <div class="abs vrule" style="left:532px;top:516px;height:204px"></div>
  <section class="abs svc" style="left:16px">
    <h2>Biodiversity and Conservation</h2>
    <div class="svc-photo" role="img" aria-label="Photo of green rainforest leaves" style="background:#4f8a22"></div>
    <p>Fauna and Flora survey, assessment, management, monitoring &amp; research, protected areas &amp; endangered &amp; threatend species.</p>
    <a class="btn">READ MORE</a>
  </section>
  <section class="abs svc" style="left:193px">
    <h2>Social &amp; Community</h2>
    <div class="svc-photo" role="img" aria-label="Photo of a community gathering" style="background:#8a5a3a"></div>
    <p>impact, stakeholder engagement, census and survey, land and community affairs, capacity building empowerment.</p>
    <a class="btn">READ MORE</a>
  </section>
  <section class="abs svc" style="left:368px">
    <h2>Environmental Management</h2>
    <div class="svc-photo" role="img" aria-label="Photo representing environmental care" style="background:#b9cf98"></div>
    <p>sustainable use, enterprise development &amp; management, biodiversity offsets.</p>
    <a class="btn">READ MORE</a>
  </section>
  <section class="abs svc" style="left:544px">
    <h2>Register With Us!</h2>
    <div class="svc-photo" role="img" aria-label="Photo of villagers gathered outdoors" style="background:#7a5e42"></div>
    <p>With the conviction that people's participation is the key to successful and sustainable development,</p>
    <a class="btn">READ MORE</a>
  </section>
  <div class="abs footer-band"></div>
  <footer class="abs footer">
    Home &nbsp;|&nbsp; About Us &nbsp;|&nbsp; What We Do &nbsp;|&nbsp; Partners &nbsp;|&nbsp; Assest Development &nbsp;|&nbsp; Resource Center &nbsp;|&nbsp; Contact us<br>
    Terms &amp; Conditions | Copyright Kunai Environment © 2012
  </footer>
</main>
</body>
</html>
```